Corporate consulting business needs a business card

I want a professional business card.... surprise me

Updates

Reason: i dont think 2 days is enough

Target Market(s)

Corprorate and Not for Profit firms and organisations

Industry/Entity Type

Consulting

Contact Information for Business Card

Logo
Corporate Consulting Services
On Time, On Budget, Beyond Expectation
Tovan Presfield
Director
0427 31 94 62 (Larger)
tovan@tp-advisory.com.au
www.tp-advisory.com.au
include little icons beside the contact info:

- Envelope = email
- Phone = phone
- Globe = website

Font styles to use
Serif
Sans Serif

Requirements
Must have
• Professional and clean
Nice to have
• you tell me

```html
<!DOCTYPE html>
<html lang="en">
<head>
<meta charset="utf-8">
<title>TP Advisory – Business Card</title>
<link rel="stylesheet" href="https://fonts.googleapis.com/css2?family=Open+Sans:wght@400;700&family=Cinzel:wght@400;700&display=swap">
<style>
  :root {
    --backdrop: #e8e5e2;
    --card: #ffffff;
    --ink: #3a2017;
    --text: #2b2b2b;
    --muted: #555555;
  }
  * { box-sizing: border-box; margin: 0; padding: 0; }
  html, body { width: 1200px; height: 997px; overflow: hidden; }
  body {
    background: var(--backdrop);
    font-family: "Open Sans", Arial, sans-serif;
    display: flex;
    flex-direction: column;
    align-items: center;
    justify-content: center;
    gap: 60px;
  }
  .card {
    position: relative;
    width: 620px;
    height: 378px;
    background: var(--card);
    box-shadow: 0 6px 18px rgba(0,0,0,0.12);
    overflow: hidden;
  }
  /* Back side */
  .card-back .brand {
    position: absolute;
    left: 0; right: 0; top: 120px;
    display: flex; align-items: center; justify-content: center; gap: 16px;
  }
  .brand-dot {
    width: 22px; height: 22px; border-radius: 50%;
    background: var(--ink);
  }
  .brand-name {
    font-family: "Cinzel", Georgia, serif;
    font-weight: 700;
    color: var(--ink);
    font-size: 40px;
    letter-spacing: 2px;
  }
  .card-back .web {
    position: absolute;
    left: 0; right: 0; bottom: 80px;
    text-align: center;
    font-size: 17px;
    color: var(--text);
  }
  /* Front side */
  .card-front .brand {
    position: absolute;
    left: 40px; top: 140px; width: 250px;
    display: flex; align-items: center; justify-content: center; gap: 12px;
  }
  .card-front .brand-name { font-size: 30px; }
  .card-front .brand-dot { width: 18px; height: 18px; }
  .divider {
    position: absolute; left: 0; top: 0;
  }
  .contact {
    position: absolute;
    left: 340px; top: 70px;
  }
  .contact .name {
    font-weight: 700; color: var(--ink); font-size: 21px;
  }
  .contact .role {
    color: var(--muted); font-size: 15px; margin-bottom: 18px;
  }
  .contact ul { list-style: none; }
  .contact li {
    display: flex; align-items: center; gap: 9px;
    font-size: 15px; color: var(--text); line-height: 25px;
  }
  .contact li.phone { font-size: 17px; }
  .contact svg { width: 15px; height: 15px; fill: var(--ink); flex: none; }
  .band-rule {
    position: absolute; left: 0; right: 0; bottom: 46px;
    height: 2px; background: var(--ink);
  }
  .band {
    position: absolute; left: 0; right: 0; bottom: 0;
    height: 40px; background: var(--ink);
  }
</style>
</head>
<body>
  <section class="card card-back">
    <div class="brand">
      <span class="brand-dot"></span>
      <span class="brand-name">TP Advisory</span>
    </div>
    <p class="web">www.tp-advisory.com.au</p>
  </section>

  <section class="card card-front">
    <div class="brand">
      <span class="brand-dot"></span>
      <span class="brand-name">TP Advisory</span>
    </div>
    <svg class="divider" width="620" height="378" viewBox="0 0 620 378" aria-hidden="true">
      <line x1="300" y1="60" x2="330" y2="260" stroke="#bdbdbd" stroke-width="1"/>
    </svg>
    <div class="contact">
      <p class="name">Tovan Presfield</p>
      <p class="role">Director</p>
      <ul>
        <li class="phone">
          <svg viewBox="0 0 16 16"><path d="M3 1h3l1 4-2 1a9 9 0 0 0 5 5l1-2 4 1v3c0 1-1 2-2 2A13 13 0 0 1 1 3c0-1 1-2 2-2z"/></svg>
          0427 31 94 62
        </li>
        <li>
          <svg viewBox="0 0 16 16"><path d="M1 3h14v10H1z M2 4l6 5 6-5" fill="none" stroke="#3a2017" stroke-width="1.6"/></svg>
          tovan@tp-advisory.com.au
        </li>
        <li>
          <svg viewBox="0 0 16 16"><g fill="none" stroke="#3a2017" stroke-width="1.3"><circle cx="8" cy="8" r="6.5"/><ellipse cx="8" cy="8" rx="3" ry="6.5"/><path d="M1.5 8h13M3 4.5h10M3 11.5h10"/></g></svg>
          www.tp-advisory.com.au
        </li>
      </ul>
    </div>
    <div class="band-rule"></div>
    <div class="band"></div>
  </section>
</body>
</html>
```